KVT Roofing Pty Ltd

We are a high end residential Roofing company
We would like something silimar to the attached logo with the same color scheme

Target Market(s)

High end residential Builders & Architects

Industry/Entity Type

Residential

```html
<!DOCTYPE html>
<html lang="en">
<head>
<meta charset="utf-8">
<title>KVT Roofing – Business Card</title>
<link rel="stylesheet" href="https://fonts.googleapis.com/css2?family=Arimo:wght@400;700&display=swap">
<style>
  :root {
    --slate: #44535e;
    --slate-text: #3f4d58;
    --blue: #1a98cf;
    --paper: #ffffff;
    --stage: #e8e5e1;
    --edge: #a9a9a9;
    --ghost: #f1f1f1;
  }
  * { box-sizing: border-box; margin: 0; padding: 0; }
  html, body { width: 1100px; height: 1200px; overflow: hidden; }
  body {
    position: relative;
    background: var(--stage);
    font-family: "Arimo", Arial, sans-serif;
    color: var(--slate-text);
  }
  .card {
    position: absolute;
    background: var(--paper);
    border: 1.5px solid var(--edge);
    border-radius: 26px;
    overflow: hidden;
  }
  .card--front { left: 136px; top: 97px; width: 821px; height: 467px; }
  .card--back  { left: 138px; top: 624px; width: 823px; height: 468px; }

  .brand-block { position: absolute; left: 49px; top: 33px; }
  .brand-square { width: 188px; height: 157px; background: var(--slate); }
  .brand-name {
    margin-top: 10px;
    font-weight: 700;
    font-size: 17px;
    line-height: 20px;
    letter-spacing: 0.3px;
    color: var(--slate-text);
    white-space: nowrap;
  }

  .holder { position: absolute; left: 36px; top: 262px; font-size: 28px; line-height: 34px; font-weight: 700; color: var(--slate-text); white-space: nowrap; }
  .holder .role { font-size: 24px; font-weight: 400; color: var(--blue); margin-left: 4px; }

  .contact { position: absolute; left: 36px; font-size: 21px; line-height: 26px; display: flex; align-items: center; gap: 8px; color: #2d2d2d; white-space: nowrap; }
  .contact--phone { top: 314px; }
  .contact--email { top: 355px; }
  .contact svg { width: 16px; height: 16px; fill: var(--blue); }

  .ghost-square { position: absolute; left: 608px; top: 248px; width: 157px; height: 125px; background: var(--ghost); }

  .bands { position: absolute; left: 0; top: 0; width: 100%; height: 100%; }
  .address {
    position: absolute; right: 42px; top: 410px;
    font-size: 21px; line-height: 26px; color: #ffffff; white-space: nowrap;
  }

  .back-panel {
    position: absolute; left: 213px; top: 61px; width: 401px; height: 334px;
    background: var(--slate);
    display: flex; align-items: center; justify-content: center;
  }
  .back-panel .brand-name { margin: 0; color: #ffffff; font-size: 28px; line-height: 34px; }
</style>
</head>
<body>
  <section class="card card--front">
    <svg class="bands" viewBox="0 0 524 298" preserveAspectRatio="none" aria-hidden="true">
      <polygon points="0,258 219,258 206,271 0,271" fill="var(--blue)"/>
      <polygon points="233,258 524,258 524,298 0,298 0,281 207,281" fill="var(--slate)"/>
    </svg>

    <div class="brand-block">
      <div class="brand-square"></div>
      <p class="brand-name">NORVALE CONSTRUCTION</p>
    </div>

    <p class="holder">Callum Ashford,<span class="role">General Manager</span></p>

    <p class="contact contact--phone">
      <svg viewBox="0 0 24 24" aria-hidden="true"><path d="M6.6 10.8a15.1 15.1 0 0 0 6.6 6.6l2.2-2.2a1 1 0 0 1 1-.25 11.4 11.4 0 0 0 3.6.57 1 1 0 0 1 1 1V20a1 1 0 0 1-1 1A17 17 0 0 1 3 4a1 1 0 0 1 1-1h3.5a1 1 0 0 1 1 1c0 1.250.2 2.450.57 3.57a1 1 0 0 1-.25 1z"/></svg>
      0400 517 286
    </p>
    <p class="contact contact--email">
      <svg viewBox="0 0 24 24" aria-hidden="true"><path d="M2 5h20v14H2z M2 5l10 8 10-8" /></svg>
      cashford@kvtroofing.com.au
    </p>

    <div class="ghost-square"></div>
    <p class="address">12 Harbour Lane, Southbank</p>
  </section>

  <section class="card card--back">
    <div class="back-panel">
      <p class="brand-name">NORVALE CONSTRUCTION</p>
    </div>
  </section>
</body>
</html>
```